Business Card and Letterhead for Vantage Psychology

We need a business card design and letterhead to use for our Psychology firm that specializes in psychoeducational assessments and individual therapy. Our motto is Purpose-Driven Assessments, Meaning-Centered Therapy.Our contact information is as follows:
Vantage Psychology
The Marwick Block - 6127-48St.
Box 2716 Olds, AB
T2K 3M8
t 403.555.0148 (VANT)
f 403.555.0172
www.vantagepsychology-example.ca
The business card will be used for two different psychologists so I can supply names nearer to completion. We prefer clean, uncluttered looks.

Target Market(s)

Clients, Educators

Font styles to use
Sans Serif

Colors

Designer to choose colors to be used in the design.

Requirements
Must have
• All relevant contact info, logo, some "white" space.
Nice to have
• It would be nice to see letterhead options that have the logo on the top of the page but also options that have it on the side. I think top of the page is probably our preference.
Should not have
• Too much clutter!

```html
<!DOCTYPE html>
<html lang="en">
<head>
<meta charset="utf-8">
<title>Vantage Psychology Letterhead</title>
<link href="https://fonts.googleapis.com/css2?family=Arimo:wght@400;700&display=swap" rel="stylesheet">
<style>
  :root {
    --backdrop: #3b3b3d;
    --paper: #ffffff;
    --teal: #4fc1da;
    --orange: #f7a842;
    --ink: #3a3a3a;
    --ink-soft: #5b5b5b;
  }
  * { box-sizing: border-box; margin: 0; padding: 0; }
  html, body {
    width: 1200px; height: 900px; overflow: hidden;
    background: var(--backdrop);
    font-family: "Arimo", Arial, sans-serif;
  }
  .letterhead {
    position: absolute; left: 290px; top: 12px;
    width: 620px; height: 876px;
    background: var(--paper);
    overflow: hidden;
    box-shadow: 0 4px 14px rgba(0,0,0,.35);
  }
  .brand {
    position: absolute; left: 72px; top: 104px;
    display: flex; align-items: center; gap: 6px;
  }
  .brand-dot {
    width: 12px; height: 12px; border-radius: 50%;
    background: var(--teal);
  }
  .brand-name {
    font-size: 11px; font-weight: 400; letter-spacing: .05em;
    color: var(--teal); text-transform: uppercase;
  }
  .contact {
    position: absolute; left: 304px; top: 98px;
    display: flex; gap: 12px;
    font-size: 7.6px; line-height: 10.5px; color: var(--ink-soft);
  }
  .contact-item { display: flex; gap: 4px; }
  .contact-item svg { flex: none; margin-top: 1px; }
  .letter-body {
    position: absolute; left: 81px; top: 207px; width: 457px;
    font-size: 8.9px; line-height: 11px; color: var(--ink);
  }
  .recipient { margin-bottom: 22px; }
  .letter-body p { text-align: justify; margin-bottom: 11px; }
  .closing { margin-top: 44px; }
  .signature { margin-top: 44px; }
  .footer-rule {
    position: absolute; left: 0; bottom: 56px; width: 620px; height: 5px;
    background: var(--orange);
  }
  .footer-band {
    position: absolute; left: 0; bottom: 0; width: 620px; height: 52px;
    background: var(--teal);
  }
  .footer-url {
    position: absolute; right: 95px; bottom: 21px;
    font-size: 9.4px; color: #fff;
  }
  .footer-url strong { font-weight: 700; }
</style>
</head>
<body>
<main class="letterhead">
  <header>
    <div class="brand">
      <span class="brand-dot"></span>
      <span class="brand-name">Vantage Psychology</span>
    </div>
    <div class="contact">
      <div class="contact-item">
        <svg width="6" height="8" viewBox="0 0 6 8"><path d="M3 0a3 3 0 0 0-3 3c0 2 3 5 3 5s3-3 3-5a3 3 0 0 0-3-3zm0 4.2A1.2 1.2 0 1 1 3 1.8a1.2 1.2 0 0 1 0 2.4z" fill="var(--teal)"/></svg>
        <address style="font-style:normal">The Marwick Block - 6127-48St.<br>Box 2716 Olds, AB T2K 3M8</address>
      </div>
      <div class="contact-item">
        <svg width="7" height="18" viewBox="0 0 7 18"><path d="M1.5 0.5l1.2 1.8-0.8 0.8c0.4 1 1.1 1.7 2 2l0.8-0.8 1.8 1.2-0.9 1.2C3.3 6.4 0.6 3.7 0.3 1.4z" fill="var(--teal)"/><rect x="0.5" y="11" width="6" height="4" rx="0.6" fill="var(--teal)"/><rect x="1.7" y="9.5" width="3.6" height="2" fill="var(--teal)"/></svg>
        <div>403.555.0148 (VANT)<br>403.555.0172</div>
      </div>
    </div>
  </header>

  <section class="letter-body">
    <div class="recipient">
      Mr. Daniel Hart<br>Managing Director<br>Northfield Capital<br>240 W Lake Avenue<br>USA
    </div>
    <p>Lorem ipsum dolor sit amet, consectetuer adipiscing elit. Nam cursus. Morbi ut mi. Nullam enim leo, egestas id, condimentum at, laoreet mattis, massa. Sed eleifend nonummy diam. Praesent mauris ante, elementum et, bibendum at, posuere sit amet, nibh. Duis tincidunt lectus quis dui viverra vestibulum.</p>
    <p>Suspendisse vulputate aliquam dui. Nulla elementum dui ut augue. Aliquam vehicula mi at mauris. Maecenas placerat, nisl at consequat rhoncus, sem nunc gravida justo, quis eleifend arcu velit quis lacus. Morbi magna magna, tincidunt a, mattis non, imperdiet vitae, tellus. Sed odio est, auctor ac, sollicitudin in, consequat vitae, orci. Fusce id felis. Vivamus sollicitudin.</p>
    <p>Suspendisse vulputate aliquam dui. Nulla elementum dui ut augue. Aliquam vehicula mi at mauris. Maecenas placerat, nisl at consequat rhoncus, sem nunc gravida justo, quis eleifend arcu velit quis lacus. Morbi magna magna, tincidunt a, mattis non, imperdiet vitae, tellus. Sed odio est, auctor ac, sollicitudin in, consequat vitae, orci. Fusce id felis. Vivamus sollicitudin.</p>
    <p>Mauris nunc quam, venenatis nec, euismod sit amet, egestas placerat, est. Pellentesque habitant morbi tristique senectus et netus et malesuada fames ac turpis egestas. Cras id elit. Integer quis urna. Ut ante enim, dapibus malesuada, fringilla eu, condimentum quis, tellus. Aenean porttitor eros vel dolor. Donec convallis pede venenatis nibh. Duis quam. Nam eget.</p>
    <p>Mauris nunc quam, venenatis nec, euismod sit amet, egestas placerat, est. Pellentesque habitant morbi tristique senectus et netus et malesuada fames ac turpis egestas. Cras id elit. Integer quis urna. Ut ante enim, dapibus malesuada, fringilla eu, condimentum quis, tellus. Aenean porttitor eros vel dolor. Donec convallis pede venenatis nibh. Duis quam. Nam eget.</p>
    <p>Mauris nunc quam, venenatis nec, euismod sit amet, egestas placerat, est. Pellenteames ac turpis egestas. Cras id elit. Integer quis urna. Ut ante enim, dapibus malesuada, fringilla eu, condimentum quis, tellus. Aenean porttitor eros vel dolor. Donec convallis pede venenatis nibh. Duis quam. Nam eget.</p>
    <div class="closing">Thank you for being one of our valued customers.</div>
    <div class="signature">Name Here<br>CEO</div>
  </section>

  <footer>
    <div class="footer-rule"></div>
    <div class="footer-band"></div>
    <div class="footer-url">www.<strong>vantagepsychology-example</strong>.ca</div>
  </footer>
</main>
</body>
</html>
```